Customer Value Leaflet

We need a bi-fold brochure designing, based on the attached PDF wireframes. Our company name is quillbrookery.com (of which the logo is currently being designed). The corporate colour is orange (the exact shade of which we are happy to leave to the designers discretion).

The leaflet will distributed to customer experience experts and marketers so the design needs to be bright, engaging, clean and simple. Design is critical.

```html
<!DOCTYPE html>
<html lang="en">
<head>
<meta charset="utf-8">
<title>Customer Value Leaflet – quillbrookery.com</title>
<link rel="stylesheet" href="https://fonts.googleapis.com/css2?family=Montserrat:wght@600;700;800&family=Open+Sans:wght@400;600;700&display=swap">
<style>
  :root {
    --brand: #f68b1f;
    --brand-text: #e7760c;
    --brand-light: #fbb26a;
    --slate: #34384f;
    --slate-deep: #2c3045;
    --slate-shadow: #1f2233;
    --arrow: #d9640a;
    --arrow-shadow: #9c4706;
    --white: #ffffff;
  }
  * { box-sizing: border-box; margin: 0; padding: 0; }
  html, body { width: 1200px; height: 849px; overflow: hidden; background: var(--white); }
  body { font-family: "Open Sans", Arial, sans-serif; }

  .spread { position: relative; width: 1200px; height: 849px; }
  .panel { position: absolute; top: 0; height: 849px; width: 600px; }
  .panel--inside { left: 0; background: var(--white); }
  .panel--cover { left: 600px; background: var(--brand); }

  /* Inside panel */
  .intro {
    position: absolute; left: 40px; top: 38px; width: 196px;
    color: var(--brand-text); font-size: 15px; line-height: 17px;
  }
  .intro__lead { font-weight: 700; margin-bottom: 17px; }
  .intro strong { font-weight: 700; }

  .gauge-photo {
    position: absolute; left: 265px; top: 30px; width: 285px; height: 215px;
    background: radial-gradient(circle at 62% 58%, #f2f2f2 0%, #c9cbcd 45%, #7d8186 75%, #e8e8e8 100%);
  }

  .clv-panel {
    position: absolute; left: 41px; top: 287px; width: 517px; height: 520px;
    background: var(--brand);
  }
  .clv-panel__tab {
    position: absolute; left: 104px; top: 0; width: 312px; height: 40px;
    background: var(--slate); border-radius: 0 0 14px 14px;
    color: var(--white); font-size: 18px; text-align: center; line-height: 40px;
  }
  .flow-arrow { position: absolute; left: 226px; top: 53px; }

  .persona { position: absolute; width: 190px; text-align: center; color: var(--white); }
  .persona--kim { left: 36px; top: 73px; }
  .persona--kevin { left: 291px; top: 73px; }
  .persona__avatar {
    display: block; margin: 0 auto; width: 100px; height: 100px; border-radius: 50%;
    background: radial-gradient(circle, #f4f4f4 0%, #e3e3e3 70%);
    border: 4px solid var(--brand-light); box-shadow: 0 0 0 2px var(--white);
  }
  .persona__name { font-family: "Montserrat", Arial, sans-serif; font-weight: 800; font-size: 19px; margin-top: 6px; line-height: 20px; }
  .persona__value { font-family: "Montserrat", Arial, sans-serif; font-weight: 700; font-size: 14px; line-height: 16px; }

  .insight {
    position: absolute; top: 245px; width: 190px; height: 131px;
    background: var(--slate-deep); color: var(--white);
    font-size: 15px; line-height: 17px; padding: 13px 26px 0 24px;
    box-shadow: 4px 4px 0 var(--slate-shadow);
  }
  .insight--kim { left: 32px; }
  .insight--kevin { left: 297px; }

  .clv-panel__footer {
    position: absolute; left: 37px; top: 455px; width: 460px;
    color: var(--white); font-size: 15px; line-height: 17px;
  }
  .clv-panel__footer strong { font-weight: 700; }

  /* Cover panel */
  .cover-photo {
    position: absolute; left: 0; top: 0; width: 600px; height: 505px;
    background: linear-gradient(100deg, #e3ded8 0%, #d2ccc4 30%, #6b5444 52%, #4a3a30 65%, #c9c2b9 85%, #e7e3de 100%);
  }
  .cover-photo__band {
    position: absolute; left: 0; top: 458px; width: 600px; height: 47px;
    background: rgba(52, 56, 79, 0.55);
  }
  .cover-title {
    position: absolute; left: 0; top: 562px; width: 600px; text-align: center; color: var(--white);
    font-weight: 400;
  }
  .cover-title__pre, .cover-title__post { font-size: 29px; line-height: 36px; font-weight: 400; }
  .cover-title__main {
    font-family: "Montserrat", Arial, sans-serif; font-weight: 700;
    font-size: 49px; line-height: 50px; letter-spacing: 1px;
  }
  .cover-footer {
    position: absolute; left: 0; top: 800px; width: 600px; height: 49px;
    background: var(--slate); color: var(--white);
    font-size: 18px; line-height: 49px; text-align: center;
  }
</style>
</head>
<body>
<div class="spread">
  <section class="panel panel--inside">
    <div class="intro">
      <p class="intro__lead">Tempora is our Customer Value Platform, designed for Marketers in the Digital Enterprise.</p>
      <p>Tempora is like having a team of <strong>data scientists</strong> making valuable insights available to your website in real-time so you can deliver the ultimate <strong>customer experience</strong>.</p>
    </div>
    <div class="gauge-photo" role="img" aria-label="Photo of a metallic gauge dial labelled Experience with its needle pointing to maximum"></div>

    <div class="clv-panel">
      <div class="clv-panel__tab">Once you can calculate CLV…</div>

      <svg class="flow-arrow" width="70" height="395" viewBox="0 0 70 395">
        <polygon points="19,0 55,0 55,358 69,358 37,393 5,358 19,358" fill="var(--arrow-shadow)"/>
        <polygon points="15,-2 51,-2 51,355 65,355 33,390 1,355 15,355" fill="var(--arrow)"/>
        <text x="33" y="178" transform="rotate(-90 33 178)" text-anchor="middle" dominant-baseline="central"
              fill="#ffffff" font-family="Montserrat, Arial, sans-serif" font-weight="800" font-size="19" letter-spacing="1">OPTIMISE YOUR MARKETING</text>
      </svg>

      <div class="persona persona--kim">
        <span class="persona__avatar" role="img" aria-label="Illustration of a woman named Kim"></span>
        <p class="persona__name">KIM</p>
        <p class="persona__value">CLV of £149</p>
      </div>
      <div class="persona persona--kevin">
        <span class="persona__avatar" role="img" aria-label="Illustration of a man named Kevin"></span>
        <p class="persona__name">KEVIN</p>
        <p class="persona__value">CLV of £282</p>
      </div>

      <div class="insight insight--kim">you can personalise Kim's marketing experience to grow her lifetime value to be more like Kevin's</div>
      <div class="insight insight--kevin">you can understand why Kevin is more valuable and acquire more customers like him</div>

      <p class="clv-panel__footer">We use data and science to <strong>predict how your customers will behave in future</strong>. Even if you already use CLV we can help you do and earn more… <strong>quillbrookery.com</strong></p>
    </div>
  </section>

  <section class="panel panel--cover">
    <div class="cover-photo" role="img" aria-label="Photo of a smiling woman holding a product in a bright shop aisle"></div>
    <div class="cover-photo__band"></div>
    <h1 class="cover-title">
      <span class="cover-title__pre">We're a</span><br>
      <span class="cover-title__main">CUSTOMER<br>VALUE</span><br>
      <span class="cover-title__post">company</span>
    </h1>
    <div class="cover-footer">quillbrookery.com | 0845 000 7312</div>
  </section>
</div>
</body>
</html>
```